Valbrook Data Works

Our company is about IT hardwares and IT solutions. IT hardware such as PC, RAMS, storage and servers. IT solutions such as project management, BA. We are also selling new technology too.

Target Market(s)

Consumer, Small to Medium Business, Corporate

Requirements
Must have
• The business card must have the following:
• Name:
• Title:
• Contact Number:
• Email address:
• Website:
• Color: Must match the logo color upgrade

```html
<!DOCTYPE html>
<html lang="en">
<head>
<meta charset="utf-8">
<title>Valbrook Data Works — Business Card</title>
<link rel="stylesheet" href="https://fonts.googleapis.com/css2?family=Oswald:wght@600&family=Montserrat:wght@500;700&family=Open+Sans:wght@400;500&display=swap">
<style>
  :root {
    --orange: #c96a26;
    --orange-soft: #d98a3e;
    --charcoal: #2c2c2e;
    --ink: #3a3a3c;
    --paper: #ffffff;
    --paper-shade: #ececec;
    --backdrop: #e9e9e9;
    --peach: #fbdfc3;
    --mist: #c7c5c3;
  }
  * { margin: 0; padding: 0; box-sizing: border-box; }
  html, body { width: 1200px; height: 1200px; overflow: hidden; }
  body { background: var(--backdrop); position: relative; }

  .card {
    position: absolute;
    top: 190px;
    width: 470px;
    height: 820px;
    background: var(--paper);
    overflow: hidden;
    box-shadow: 0 10px 30px rgba(0,0,0,0.18);
  }
  .card--front { left: 100px; }
  .card--back { left: 630px; }
  .card__art { position: absolute; inset: 0; width: 100%; height: 100%; }

  .brand { position: absolute; left: 0; right: 0; text-align: center; }
  .brand__dot {
    display: block;
    margin: 0 auto 22px;
    width: 62px; height: 62px;
    border-radius: 50%;
    background: var(--orange);
  }
  .brand__name {
    font-family: "Oswald", sans-serif;
    font-weight: 600;
    color: var(--ink);
    text-transform: uppercase;
    line-height: 1.05;
    letter-spacing: 1px;
  }
  .card--front .brand { top: 475px; }
  .card--front .brand__name { font-size: 46px; }
  .card--back .brand { top: 55px; }
  .card--back .brand__dot { width: 54px; height: 54px; margin-bottom: 18px; }
  .card--back .brand__name { font-size: 40px; }

  .holder { position: absolute; top: 395px; left: 0; right: 0; text-align: center; }
  .holder__name {
    font-family: "Montserrat", sans-serif;
    font-size: 38px;
    letter-spacing: 0.5px;
    text-transform: uppercase;
    color: var(--ink);
    font-weight: 500;
  }
  .holder__first { color: var(--orange); font-weight: 700; }
  .holder__title {
    font-family: "Open Sans", sans-serif;
    font-size: 22px;
    font-weight: 500;
    color: var(--ink);
    margin-top: 6px;
  }
  .holder__rule {
    width: 200px; height: 3px; margin: 8px auto 0;
    background: linear-gradient(90deg, transparent, rgba(0,0,0,0.25), transparent);
  }

  .contacts {
    position: absolute; top: 540px; left: 72px; right: 30px;
    list-style: none;
  }
  .contacts__item {
    display: flex; align-items: center;
    height: 70px;
    font-family: "Open Sans", sans-serif;
    font-size: 19px;
    color: var(--charcoal);
  }
  .contacts__icon { width: 52px; height: 58px; flex: none; margin-right: 24px; }
  .contacts__link {
    position: absolute; left: 25px; top: 30px;
    width: 2px; height: 140px; background: var(--charcoal);
  }
</style>
</head>
<body>

  <!-- Front of card -->
  <section class="card card--front">
    <svg class="card__art" viewBox="0 0 470 820" aria-hidden="false">
      <defs>
        <linearGradient id="hardwareTone" x1="0" y1="0" x2="1" y2="1">
          <stop offset="0" stop-color="#1e1e1e"/>
          <stop offset="0.5" stop-color="#6d6d6d"/>
          <stop offset="1" stop-color="#2a2a2a"/>
        </linearGradient>
      </defs>
      <rect class="hero-photo" x="0" y="0" width="470" height="440" fill="url(#hardwareTone)" role="img" aria-label="Black and white close-up photo of computer hardware: motherboard, cooling tubes and cables"/>
      <rect x="0" y="300" width="470" height="180" fill="var(--charcoal)"/>
      <polygon points="0,355 235,238 470,345 470,820 0,820" fill="var(--paper-shade)"/>
      <polygon points="0,395 235,270 470,385 470,820 0,820" fill="var(--orange)"/>
      <polygon points="0,440 235,305 470,430 470,820 0,820" fill="var(--paper)"/>
      <rect x="150" y="668" width="180" height="3" fill="var(--orange)"/>
      <rect x="165" y="680" width="140" height="3" fill="var(--orange)"/>
      <rect x="0" y="708" width="470" height="40" fill="var(--orange)"/>
      <rect x="0" y="748" width="470" height="72" fill="var(--charcoal)"/>
    </svg>
    <div class="brand">
      <span class="brand__dot"></span>
      <div class="brand__name">Valbrook<br>Data Works</div>
    </div>
  </section>

  <!-- Back of card -->
  <section class="card card--back">
    <svg class="card__art" viewBox="0 0 470 820">
      <defs>
        <linearGradient id="skyTone" x1="0" y1="0" x2="0" y2="1">
          <stop offset="0" stop-color="var(--mist)"/>
          <stop offset="0.55" stop-color="var(--peach)"/>
          <stop offset="1" stop-color="#fde9d6"/>
        </linearGradient>
      </defs>
      <rect x="0" y="0" width="470" height="440" fill="url(#skyTone)"/>
      <polygon points="0,300 0,440 470,440 470,270 400,300 235,300" fill="var(--charcoal)"/>
      <polygon points="0,350 235,245 470,340 470,820 0,820" fill="var(--paper-shade)"/>
      <polygon points="0,395 235,280 470,380 470,820 0,820" fill="var(--orange)"/>
      <polygon points="0,440 235,312 470,425 470,820 0,820" fill="var(--paper)"/>
      <rect x="0" y="762" width="470" height="58" fill="var(--charcoal)"/>
      <polygon points="0,715 58,762 0,805" fill="var(--orange)"/>
      <polygon points="470,700 410,762 470,762" fill="var(--orange)"/>
    </svg>
    <div class="brand">
      <span class="brand__dot"></span>
      <div class="brand__name">Valbrook<br>Data Works</div>
    </div>

    <div class="holder">
      <div class="holder__name"><span class="holder__first">Marlo</span> Keane</div>
      <div class="holder__title">Executive Officer</div>
      <div class="holder__rule"></div>
    </div>

    <ul class="contacts">
      <span class="contacts__link"></span>
      <li class="contacts__item">
        <svg class="contacts__icon" viewBox="0 0 52 58">
          <polygon points="26,2 50,15 50,43 26,56 2,43 2,15" fill="var(--charcoal)"/>
          <path d="M19 17c2-1 3 0 4 2l1 4c0 1-1 2-2 3 1 3 4 6 7 7 1-1 2-2 3-2l4 1c2 1 3 2 2 4-1 2-3 3-5 3-9-1-16-8-17-17 0-2 1-4 3-5z" fill="#fff"/>
        </svg>
        <span>+999 410 382 617 204</span>
      </li>
      <li class="contacts__item">
        <svg class="contacts__icon" viewBox="0 0 52 58">
          <polygon points="26,2 50,15 50,43 26,56 2,43 2,15" fill="var(--charcoal)"/>
          <rect x="14" y="20" width="24" height="17" fill="none" stroke="#fff" stroke-width="2"/>
          <polyline points="14,20 26,30 38,20" fill="none" stroke="#fff" stroke-width="2"/>
        </svg>
        <span>hello@valbrookdata.com</span>
      </li>
      <li class="contacts__item">
        <svg class="contacts__icon" viewBox="0 0 52 58">
          <polygon points="26,2 50,15 50,43 26,56 2,43 2,15" fill="var(--charcoal)"/>
          <circle cx="26" cy="29" r="12" fill="none" stroke="#fff" stroke-width="2"/>
          <ellipse cx="26" cy="29" rx="5" ry="12" fill="none" stroke="#fff" stroke-width="1.6"/>
          <line x1="14" y1="29" x2="38" y2="29" stroke="#fff" stroke-width="1.6"/>
        </svg>
        <span>www.valbrookdata.com</span>
      </li>
    </ul>
  </section>

</body>
</html>
```